Bright Leaf Company Needs New Packaging Design

We need a design to print directly on our stand up zip pouches, 6x9x3 in., to replace the labels we were applying on generic matte black pouches.

We'd like to keep the current color theme of matte black + [Flavor Color] (in this case, fushia) to communicate the idea of modern, luxury brand (please see velcorra coffee brand) and stay somewhat close to the current label so our product will be recognized by actual customers. Other flavors will be a declination of the same layout, matte black + [flavor color]. Colors used should be vibrant, eye catching, to stand out from competition.

We also want to display the actual tea blend picture on the packaging so the consumer can see how beautiful the tea is. The font size for Amber Orchard Meadow should be big enough so it's readable when the product is seen in thumbnail format.

The front should have a seal/stamp close to a top corner with a big "100% Freshness Guarantee",

The company logo "The Lumo Company" should be present on the front in a prominent spot. It's provided in the zip file from old label.

We need to display the net weight (4oz / 113g) and number of servings (makes 60 cups). Please refer to old label.

On the back side we need a space for the UPC barcode at the bottom, the company address, a space for the brand's story/mission, steeping instructions with icons (see current label), ingredients and another section featuring our other products. All fonts should be 10pt or bigger.

Artwork of the current label current label is available here
https://files.zentrovault.example/folders/7Qx2mRpL4vNa8sKd1TyHwBcE?resourcekey=0-Fk39LwQpz8RnVt2XyMbCaJ&usp=sharing

Target Market(s)

USA market, Women ages 25-45, young & young at heart, trendy, health conscious, luxury

Industry/Entity Type

Premium Loose Leaf Tea

Font styles to use
Other font styles liked:
• fonts provided in zip file

Colors
E54698
E96AAD
F1A4CE
F9D9EA
FCEFF6

Requirements
Must have
• See description
Should not have
• Asian look and feel

```html
<!DOCTYPE html>
<html lang="en">
<head>
<meta charset="utf-8">
<title>The Lumo Company – Amber Orchard Meadow Tea</title>
<link href="https://fonts.googleapis.com/css2?family=Lora:ital,wght@0,400;0,600;0,700;1,400;1,600;1,700&display=swap" rel="stylesheet">
<style>
  :root {
    --stage: #f4f3f3;
    --pouch: #161616;
    --pouch-edge: #2a2a2a;
    --zip: #3a3a3a;
    --label-top: #fdfafc;
    --label-pink: #f4d9e8;
    --blob: #f8e3ee;
    --plum: #7a1f4a;
    --brand: #8c2b62;
    --seal: #e54698;
    --seal-ring: #f9d9ea;
    --seal-dark: #4a1030;
    --gold: #e9ad12;
    --ink: #111111;
    --white: #ffffff;
    --blend-gold: #d9b640;
    --blend-rose: #b5475f;
    --blend-amber: #e2a92a;
  }
  * { margin: 0; padding: 0; box-sizing: border-box; }
  html, body { width: 1200px; height: 675px; overflow: hidden; }
  body {
    background: var(--stage);
    font-family: "Lora", Georgia, serif;
    position: relative;
  }

  /* Pouch front print */
  .pouch {
    position: absolute;
    left: 404px;
    top: 36px;
    width: 400px;
    height: 590px;
    background: var(--pouch);
    border: 1px solid var(--pouch-edge);
  }
  .pouch__zip {
    position: absolute;
    left: 16px; right: 16px; top: 80px;
    height: 3px;
    background: var(--zip);
  }
  .pouch__zip--lower { top: 86px; height: 1px; }

  .label {
    position: absolute;
    left: 70px;
    top: 148px;
    width: 263px;
    height: 390px;
    overflow: hidden;
    background: linear-gradient(180deg, var(--label-top) 0%, var(--label-pink) 100%);
  }
  .label__blobs, .label__blend { position: absolute; left: 0; top: 0; width: 263px; height: 390px; }

  .brand {
    position: absolute;
    left: 0; right: 0; top: 48px;
    display: flex; align-items: center; justify-content: center; gap: 6px;
    color: var(--brand);
    font-weight: 700;
    font-size: 17px;
  }
  .brand__dot { width: 9px; height: 9px; border-radius: 50%; background: var(--brand); }

  .seal {
    position: absolute;
    left: 18px; top: 108px;
    width: 78px; height: 78px;
    border-radius: 50%;
    background: var(--seal);
    border: 3px solid var(--seal-ring);
    display: flex; flex-direction: column; align-items: center; justify-content: center;
    transform: rotate(-14deg);
    color: var(--white);
    font-weight: 700;
    line-height: 1.12;
    text-align: center;
  }
  .seal__pct { font-size: 12px; color: var(--seal-dark); }
  .seal__text { font-size: 10.5px; }

  .flavor { font-weight: 700; }
  .title-box {
    position: absolute;
    background: var(--white);
    height: 32px;
    display: flex; align-items: center;
    font-size: 28px;
    line-height: 1;
    color: var(--plum);
  }
  .title-box--one { left: 73px; top: 167px; width: 104px; justify-content: center; }
  .title-box--two { left: 59px; top: 202px; width: 176px; justify-content: center; }
  .title-box--three { left: 44px; top: 238px; width: 175px; padding-left: 17px; color: var(--gold); font-style: italic; }
  .title-box--tea { left: 79px; top: 274px; width: 126px; padding-left: 20px; gap: 8px; color: var(--ink); }
  .title-box__note { font-size: 8px; font-style: italic; font-weight: 600; line-height: 1.25; }

  .facts {
    position: absolute;
    left: 20px; top: 349px;
    width: 223px; height: 24px;
    background: var(--white);
    display: flex; align-items: center; justify-content: space-between;
    padding: 0 10px;
    color: var(--plum);
  }
  .facts__cups { font-style: italic; font-size: 12px; }
  .facts__weight { font-size: 10px; color: #3a1a28; }
</style>
</head>
<body>
  <main class="pouch">
    <div class="pouch__zip"></div>
    <div class="pouch__zip pouch__zip--lower"></div>

    <section class="label">
      <svg class="label__blobs" viewBox="0 0 263 390" aria-hidden="true">
        <path d="M0 50 Q12 32 56 33 Q94 35 106 68 L106 190 L0 190 Z" fill="var(--blob)"/>
        <path d="M156 106 Q188 76 225 88 Q263 100 263 125 L263 190 L156 190 Z" fill="var(--blob)"/>
      </svg>

      <svg class="label__blend" viewBox="0 0 263 390" role="img" aria-label="Photo of the loose leaf tea blend: dried petals and golden flower buds">
        <defs>
          <linearGradient id="blend" x1="0" y1="0" x2="1" y2="1">
            <stop offset="0" stop-color="var(--blend-gold)"/>
            <stop offset="0.45" stop-color="var(--blend-rose)"/>
            <stop offset="1" stop-color="var(--blend-amber)"/>
          </linearGradient>
        </defs>
        <path d="M0 190 Q30 150 80 135 Q120 122 160 125 Q210 128 240 150 Q258 165 263 180 L263 390 L0 390 Z" fill="url(#blend)" opacity="0.9"/>
      </svg>

      <div class="brand"><span class="brand__dot"></span>The Lumo Company</div>

      <div class="seal">
        <span class="seal__pct">100%</span>
        <span class="seal__text">Freshness</span>
        <span class="seal__text">Guarantee</span>
      </div>

      <h1 class="flavor">
        <span class="title-box title-box--one">Amber</span>
        <span class="title-box title-box--two">Orchard</span>
        <span class="title-box title-box--three">Meadow</span>
        <span class="title-box title-box--tea">Tea <span class="title-box__note">Calm &amp;<br>Soothing</span></span>
      </h1>

      <div class="facts">
        <span class="facts__cups">60 cups</span>
        <span class="facts__weight">4oz / 113g</span>
      </div>
    </section>
  </main>
</body>
</html>
```